New Business Card for General Contractor Marketing

Need a business card the is more like a marketing promotion of our services
Must be horizontal orientation, One Sided Only, Max font size, Organize the Services
#1 General Contractor for Realtors
Remodels – Renovations – Repairs
Water & Mold Damage Experts
Painting: Interior/ Exterior
Flooring: Wood / LVT / Carpet
Plumbing: Repairs & Upgrades
Electric: Lights & Energy Efficient Upgrades
Kitchen & Bath Remodels
Fast Inspections Repair Billed Thru Escrow
BrightHarborBuilds.com
555-418-2796

Industry/Entity Type

General Contractor

Contact Information for Business Card

One Sided Only: #1 General Contractor for Realtors Remodels – Renovations – Repairs Water & Mold Damage Experts Painting: Interior/ Exterior Flooring: Wood / LVT / Carpet Plumbing: Repairs & Upgrades Electric: Lights & Energy Efficient Upgrades Kitchen & Bath Remodels Fast Inspections Repair Billed Thru Escrow BrightHarborBuilds.com 555-418-2796

Colors
0054AA
0677BA
7BADD7
CADEEF
E8F1F8

Requirements
Must have
• One Sided Only: #1 General Contractor for Realtors Remodels – Renovations – Repairs Water & Mold Damage Experts Painting: Interior/ Exterior Flooring: Wood / LVT / Carpet Plumbing: Repairs & Upgrades Electric: Lights & Energy Efficient Upgrades Kitchen & Bath Remodels Fast Inspections Repair Billed Thru Escrow BrightHarborBuilds.com 555-418-2796

```html
<!DOCTYPE html>
<html lang="en">
<head>
<meta charset="utf-8">
<title>Bright Harbor Builds – Business Card</title>
<link href="https://fonts.googleapis.com/css2?family=Roboto+Condensed:wght@400;700&display=swap" rel="stylesheet">
<style>
  :root {
    --backdrop: #9b9b9b;
    --card: #ffffff;
    --navy: #1b2a57;
    --orange: #f5821f;
    --ink: #111111;
  }
  * { margin: 0; padding: 0; box-sizing: border-box; }
  html, body {
    width: 1200px;
    height: 1059px;
    overflow: hidden;
    background: var(--backdrop);
    font-family: "Roboto Condensed", "Arial Narrow", sans-serif;
  }
  .card {
    position: absolute;
    left: 30px;
    top: 203px;
    width: 1140px;
    height: 652px;
    background: var(--card);
    border-radius: 36px;
    color: var(--ink);
  }
  .brand {
    position: absolute;
    left: 43px;
    top: 62px;
    width: 262px;
    display: flex;
    align-items: center;
    gap: 12px;
  }
  .brand-dot {
    width: 22px;
    height: 22px;
    background: var(--orange);
    border-radius: 50%;
    flex: none;
  }
  .brand-name {
    font-weight: 700;
    font-size: 32px;
    line-height: 1.05;
    color: var(--navy);
    letter-spacing: 0.5px;
  }
  .headline {
    position: absolute;
    left: 320px;
    top: 68px;
    width: 790px;
    text-align: center;
  }
  .headline-title {
    font-weight: 700;
    font-size: 45px;
    line-height: 1.1;
    white-space: nowrap;
  }
  .headline-sub {
    font-size: 39px;
    line-height: 1.3;
    white-space: nowrap;
  }
  .services {
    position: absolute;
    list-style: none;
  }
  .services li {
    position: relative;
    font-size: 30px;
    line-height: 54px;
    padding-left: 34px;
    white-space: nowrap;
  }
  .services li::before {
    content: "";
    position: absolute;
    left: 0;
    top: 19px;
    width: 17px;
    height: 17px;
    border-radius: 50%;
    background: var(--orange);
  }
  .services-left { left: 46px; top: 241px; }
  .services-right { left: 529px; top: 234px; }
  .promo-band {
    position: absolute;
    left: 50px;
    top: 442px;
    width: 1049px;
    height: 71px;
    background: var(--navy);
    color: #ffffff;
    display: flex;
    align-items: center;
    justify-content: center;
    gap: 14px;
    font-weight: 700;
    font-size: 44px;
    line-height: 1;
    white-space: nowrap;
  }
  .promo-dot {
    width: 26px;
    height: 26px;
    border-radius: 50%;
    background: var(--orange);
    flex: none;
  }
  .contact {
    position: absolute;
    top: 555px;
    display: flex;
    align-items: center;
    gap: 12px;
    font-size: 41px;
    line-height: 50px;
    white-space: nowrap;
  }
  .contact-web { left: 54px; }
  .contact-phone { right: 48px; }
  .contact svg { flex: none; }
</style>
</head>
<body>
  <div class="card">
    <div class="brand">
      <span class="brand-dot"></span>
      <span class="brand-name">BRIGHT HARBOR<br>BUILDS</span>
    </div>

    <div class="headline">
      <div class="headline-title">#1 GENERAL CONTRACTOR FOR REALTORS</div>
      <div class="headline-sub">Remodels – Renovations – Repairs</div>
    </div>

    <ul class="services services-left">
      <li>Water &amp; Mold Damage Experts</li>
      <li>Painting – Interior / Exterior</li>
      <li>Flooring – Wood / LVT / Carpet</li>
    </ul>
    <ul class="services services-right">
      <li>Plumbing – Repairs &amp; Upgrades</li>
      <li>Electrical – Lights &amp; Energy-Efficient Upgrades</li>
      <li>Kitchen &amp; Bath Remodels</li>
    </ul>

    <div class="promo-band">
      <span>FAST INSPECTIONS</span>
      <span class="promo-dot"></span>
      <span>REPAIR BILLED THRU ESCROW</span>
    </div>

    <div class="contact contact-web">
      <svg width="38" height="38" viewBox="0 0 38 38" aria-hidden="true">
        <circle cx="19" cy="19" r="17" fill="none" stroke="var(--orange)" stroke-width="3"/>
        <ellipse cx="19" cy="19" rx="7" ry="17" fill="none" stroke="var(--orange)" stroke-width="2.5"/>
        <line x1="2" y1="19" x2="36" y2="19" stroke="var(--orange)" stroke-width="2.5"/>
      </svg>
      <span>BrightHarborBuilds.com</span>
    </div>

    <div class="contact contact-phone">
      <svg width="46" height="34" viewBox="0 0 46 34" aria-hidden="true">
        <path d="M2 12 C2 3 44 3 44 12 L44 15 L34 15 L34 10 L12 10 L12 15 L2 15 Z" fill="var(--orange)"/>
        <path d="M13 13 L33 13 L42 30 L4 30 Z" fill="var(--orange)"/>
        <circle cx="23" cy="22" r="4" fill="#ffffff"/>
      </svg>
      <span>555-418-2796</span>
    </div>
  </div>
</body>
</html>
```